Book cover for The Quiet Lioness Manual to Turn into a Powerhouse at Work

Book cover design for soft cover non-fiction book.

The front cover is what is most important at this stage, I am still gathering the testimonials and book description for the back cover so a rough to be completed later for the back is great.

Title as per above. Divided up "The Quiet Lioness Manual" (to be a series) and "Turn into a Powerhouse at Work" in this book in the series

Also for the front:

Lorna Kevesh

"The most unusual business book you will read." - Gwen Talrowicz, Author of Founder Sunrise

Background info:

This work is a blending of the masculine and feminine energies, the practical business skills with a strong focus on the inner game. I am looking for the cover to have a nod to the Dominatrix and a clear message that one can be soft (kind, open hearted) and still be strong and firm in business.

Photo options are in this file https://www.filecrate-example.net/sh/qmx41tgbw8vkrle/BBEtmkqpQ2XrLm3nXoyy94J4b?dl=0

Size 6" x 9" 179 pgs

Target Market(s)

female entreprenures

Industry/Entity Type

Business

Colors

Designer to choose colors to be used in the design.

Requirements
Must have
• I would like the title to be in a font that is bold and upscale, to contrast the softness fo the image.
• Clear and readable
• Unique look that will stand out
Should not have
• overt Dominatrix images or slant. It is about the energy not the actual.

```html
<!DOCTYPE html>
<html lang="en">
<head>
<meta charset="utf-8">
<title>The Quiet Lioness Manual – Cover Spread</title>
<link rel="stylesheet" href="https://fonts.googleapis.com/css2?family=Montserrat:wght@400;500;700&family=Open+Sans:ital,wght@0,400;1,400&display=swap">
<style>
  :root {
    --page-bg: #f2f2f2;
    --cover-black: #000000;
    --ink-white: #ffffff;
    --spine-white: #ffffff;
    --ink-black: #111111;
    --photo-blue: #2a6f93;
    --photo-skin: #c9a08a;
    --photo-hair: #c8b48a;
  }
  * { box-sizing: border-box; margin: 0; padding: 0; }
  html, body { width: 899px; height: 1200px; overflow: hidden; }
  body { background: var(--page-bg); position: relative; }

  .cover-spread {
    position: absolute;
    left: 12px; top: 290px;
    width: 875px; height: 620px;
    display: flex;
  }

  /* Back cover */
  .back-cover {
    position: relative;
    width: 404px; height: 100%;
    background: var(--cover-black);
    color: var(--ink-white);
    padding: 28px 28px 0 26px;
  }
  .back-cover__intro {
    font-family: "Open Sans", sans-serif;
    font-size: 13.4px;
    line-height: 20.6px;
    letter-spacing: 0.3px;
    text-align: justify;
    width: 350px;
  }
  .back-cover__body {
    font-family: "Open Sans", sans-serif;
    font-style: italic;
    font-size: 10.3px;
    line-height: 15.6px;
    text-align: justify;
    width: 350px;
    margin-top: 30px;
  }
  .back-cover__body + .back-cover__body { margin-top: 12px; }
  .back-cover__isbn-box {
    position: absolute;
    left: 26px; top: 506px;
    width: 90px; height: 58px;
    background: var(--ink-white);
  }

  /* Spine */
  .spine {
    position: relative;
    width: 68px; height: 100%;
    background: var(--spine-white);
  }
  .spine__text {
    position: absolute;
    left: 50%; top: 26px;
    transform-origin: 0 0;
    transform: rotate(90deg) translateY(-50%);
    white-space: nowrap;
    display: flex; align-items: baseline; gap: 26px;
    color: var(--ink-black);
  }
  .spine__title {
    font-family: "Montserrat", sans-serif;
    font-weight: 700;
    font-size: 17.5px;
    text-transform: uppercase;
  }
  .spine__author {
    font-family: "Montserrat", sans-serif;
    font-weight: 400;
    font-size: 14px;
    letter-spacing: 7px;
    text-transform: uppercase;
  }

  /* Front cover */
  .front-cover {
    position: relative;
    width: 403px; height: 100%;
    background: var(--cover-black);
    color: var(--ink-white);
    overflow: hidden;
  }
  .front-cover__photo {
    position: absolute;
    left: 30px; top: 180px;
    width: 340px; height: 440px;
    background:
      radial-gradient(ellipse 32% 26% at 50% 30%, var(--photo-skin) 0%, rgba(201,160,138,0.6) 55%, rgba(0,0,0,0) 100%),
      radial-gradient(ellipse 40% 22% at 46% 18%, var(--photo-hair) 0%, rgba(200,180,138,0) 100%),
      radial-gradient(ellipse 60% 45% at 50% 85%, var(--photo-blue) 0%, rgba(42,111,147,0.5) 50%, rgba(0,0,0,0) 100%);
  }
  .front-cover__text { position: relative; z-index: 2; padding: 20px 0 0 22px; }
  .front-cover__subtitle {
    font-family: "Montserrat", sans-serif;
    font-weight: 500;
    font-size: 17.2px;
    letter-spacing: 0.2px;
    text-transform: uppercase;
  }
  .front-cover__title {
    font-family: "Montserrat", sans-serif;
    font-weight: 700;
    text-transform: uppercase;
    line-height: 0.98;
    margin-top: 4px;
  }
  .front-cover__title-line { display: block; font-size: 47px; letter-spacing: -0.5px; }
  .front-cover__title-line--large { font-size: 72px; letter-spacing: -1px; line-height: 1; }

  .endorsement {
    position: absolute;
    left: 278px; top: 246px;
    width: 96px; height: 96px;
    border-radius: 50%;
    background: var(--ink-white);
    color: var(--ink-black);
    z-index: 2;
    display: flex; flex-direction: column; align-items: center; justify-content: center;
    text-align: center;
  }
  .endorsement__inner { transform: rotate(18deg); width: 80px; }
  .endorsement__quote {
    font-family: "Montserrat", sans-serif;
    font-weight: 700;
    font-size: 6.6px;
    line-height: 7.8px;
    text-transform: uppercase;
  }
  .endorsement__source {
    font-family: "Open Sans", sans-serif;
    font-style: italic;
    font-size: 5.6px;
    line-height: 6.8px;
    margin-top: 3px;
  }

  .front-cover__author {
    position: absolute;
    left: 0; right: 0; top: 545px;
    z-index: 2;
    text-align: center;
    font-family: "Montserrat", sans-serif;
    font-weight: 400;
    font-size: 21px;
    letter-spacing: 5.5px;
    text-transform: uppercase;
  }
</style>
</head>
<body>
  <main class="cover-spread">
    <section class="back-cover">
      <p class="back-cover__intro">This work is a blending of the masculine and feminine energies, the practical business skills with a strong focus on the inner game. I am looking for the cover to have a nod to the Dominatrix and a clear message that one can be soft (kind, open hearted) and still be strong and firm in business.</p>
      <p class="back-cover__body">Donec vitae convallis nunc, vel ultrices nunc. Proin quis iaculis tellus. Vivamus at diam eget lectus aliquam tincidunt quis non erat. Sed non turpis mollis, ullamcorper nisi in, pretium diam. Praesent laoreet ligula in ante congue, id placerat lorem pharetra. Mauris pulvinar, metus quis iaculis consectetur, mauris massa egestas tortor, ut laoreet mauris ex in sapien. Nullam dolor neque, feugiat non arcu a, aliquet semper justo. Sed porttitor lacus elit, et feugiat felis ultricies quis. Nunc hendrerit risus non sodales tempor.</p>
      <p class="back-cover__body">Curabitur aliquet a nisl id lobortis. Class aptent taciti sociosqu ad litora torquent per conubia nostra, per inceptos himenaeos. Sed tincidunt pretium odio id pharetra. Nulla mattis est lacus. Fusce nec gravida massa. Duis eu ligula in nulla laoreet lobortis. Integer sit amet odio metus.</p>
      <div class="back-cover__isbn-box"></div>
    </section>

    <section class="spine">
      <div class="spine__text">
        <span class="spine__title">The Quiet Lioness Manual</span>
        <span class="spine__author">Lorna Kevesh</span>
      </div>
    </section>

    <section class="front-cover">
      <div class="front-cover__photo" role="img" aria-label="Portrait photo of the smiling author in a blue top, chin resting on her hand, against a black background"></div>
      <div class="front-cover__text">
        <p class="front-cover__subtitle">Turn into a Powerhouse at Work</p>
        <h1 class="front-cover__title">
          <span class="front-cover__title-line">The Quiet</span>
          <span class="front-cover__title-line">Lioness</span>
          <span class="front-cover__title-line front-cover__title-line--large">Manual</span>
        </h1>
      </div>
      <div class="endorsement">
        <div class="endorsement__inner">
          <p class="endorsement__quote">“The most unusual business book you will read.”</p>
          <p class="endorsement__source">Gwen Talrowicz, Author of Founder Sunrise</p>
        </div>
      </div>
      <p class="front-cover__author">Lorna Kevesh</p>
    </section>
  </main>
</body>
</html>
```